Luxury Inclusive Beauty Brand Needs Labels & Boxes for Product Line

We need updated labels and boxes for our cosmetic and skin care line. Our company is MAVRA & CO. and we focus on providing upscale, natural and organic beauty products inclusive of diverse and deeper skin tones for women of color, especially black women. We have a seven piece skin care collection called DERMAVELLE Baobin Collection and a mineral make-up line consisting of eight products. The design of all products should be the same with just dimensions and title/ingredient list differences. We would like to see designs that use our coral color e85350, work well on black packaging (bottles, lipstick tubes etc.) and include white and other additional pretty colors, metallics or patterns representative of ethnic (AFRICAN), bohemian or tribal influence. The final design should communicate luxury, floral/fauna environmentalism, and afrocentric culture influences.
We have included files of various prints we like and the type of lifestyle our customer aspires to/is attracted to. We have included in the files below some examples of packaging we like but we want something original to capture the attention of our target market, upper income health and ethnic conscious black women age 30 - 55 who love natural and organic products. The names of our products include the list below however if design can be submitted showing design on 1 tall box and 1 short box and 1 lipstick size box that would be great:
DERMAVELLE Baobin Collection Cleansing Oil (dropper)
DERMAVELLE Baobin Collection Balancing Toner (tall spray bottle)
DERMAVELLE Baobin Collection Moisturizing Serum (dropper)
DERMAVELLE Baobin Collection Moisturizing Cream (short box jar)
DERMAVELLE Baobin Lip Scrub (short box - jar)
Luminous Mineral Foundation (short box- jar)
CC Cream
Moisturizing Lip Stick (lipstick box)
OTIRAFLIX Natural Mascara
Zarra Bimble Lip Crayon
Gel Eye Liner
Organic Make-up Remover (tall spray bottle)
Face & Eye Primer
Final dimensions /dies of boxes can be sent to winner of design competition.
Target Market(s)
women of color, age 30-55, income 50 - 150K, natural hair and organic lifestyle, yoga
Industry/Entity Type
Cosmetics
Requirements
Must have
- label and box
- include the color e85350
- include logo
Nice to have
- easy way to differentiate skincare from make-up products

```html
<!DOCTYPE html>
<html lang="en">
<head>
<meta charset="utf-8">
<title>MAVRA &amp; CO. — DERMAVELLE Baobin Collection Packaging</title>
<link rel="stylesheet" href="https://fonts.googleapis.com/css2?family=Lato:wght@400&family=Marcellus&family=Cinzel:wght@400;600&display=swap">
<style>
  :root{
    --coral:#e85350;
    --gold:#b39a62;
    --ink:#1c1c1c;
    --paper:#ffffff;
    --stage:#ffffff;
    --pattern:linear-gradient(135deg,#f4e1a9 0%,#e97a6c 22%,#f6d3c6 40%,#e9bf5e 58%,#e85350 74%,#f7e6b6 100%);
  }
  *{box-sizing:border-box;margin:0;padding:0}
  html,body{width:1200px;height:663px;overflow:hidden;background:var(--stage)}
  .canvas{position:relative;width:1200px;height:663px;background:var(--stage)}

  .pattern{position:absolute;background:var(--pattern)}
  .piece{position:absolute;box-shadow:0 4px 10px rgba(0,0,0,.18)}

  .panel{position:absolute;background:var(--paper);border:2px solid var(--coral);
    display:flex;flex-direction:column;align-items:center;text-align:center}
  .brand{display:flex;align-items:center;gap:6px;font-family:"Lato",sans-serif;color:var(--ink);letter-spacing:.02em}
  .brand-dot{border-radius:50%;border:1.5px solid var(--ink);display:inline-block}
  .line-name{font-family:"Marcellus",serif;color:var(--gold);letter-spacing:.04em}
  .line-sub{font-family:"Marcellus",serif;color:var(--gold);letter-spacing:.08em;text-transform:uppercase}
  .band{width:calc(100% + 4px);margin-left:-2px;background:var(--coral);color:var(--paper);
    font-family:"Cinzel",serif;font-weight:600;letter-spacing:.08em;text-transform:uppercase;
    display:flex;align-items:center;justify-content:center}
  .volume{font-family:"Cinzel",serif;color:var(--ink);letter-spacing:.06em}

  /* tall box */
  .tall-box{left:228px;top:60px;width:292px;height:550px}
  .tall-box .panel{left:22px;top:26px;width:246px;height:230px}
  .tall-box .brand{margin-top:36px;font-size:18px}
  .tall-box .brand-dot{width:14px;height:14px}
  .tall-box .line-name{margin-top:18px;font-size:22px}
  .tall-box .line-sub{margin-top:4px;font-size:12.5px}
  .tall-box .band{margin-top:16px;height:27px;font-size:15px}
  .tall-box .volume{margin-top:22px;font-size:10px}

  /* short box */
  .short-box{left:551px;top:60px;width:283px;height:306px}
  .short-box .panel{left:21px;top:36px;width:240px;height:233px}
  .short-box .brand{margin-top:38px;font-size:18px}
  .short-box .brand-dot{width:14px;height:14px}
  .short-box .line-name{margin-top:20px;font-size:22px}
  .short-box .line-sub{margin-top:4px;font-size:12.5px}
  .short-box .band{margin-top:16px;height:25px;font-size:13.5px}
  .short-box .volume{margin-top:24px;font-size:10px}

  /* lipstick box */
  .lip-box{left:1015px;top:55px;width:109px;height:480px}
  .lip-box .panel{left:5px;top:125px;width:94px;height:96px}
  .lip-box .brand{margin-top:22px;font-size:10px;gap:4px}
  .lip-box .brand-dot{width:8px;height:8px;border-width:1px}
  .lip-box .lip-title{margin-top:14px;font-family:"Cinzel",serif;font-weight:600;color:var(--coral);
    font-size:10px;letter-spacing:.06em;line-height:1.5;text-transform:uppercase}

  /* spray bottle label */
  .spray-label{left:51px;top:289px;width:127px;height:280px}
  .spray-label .panel{left:11px;top:60px;width:108px;height:120px}
  .spray-label .brand{margin-top:12px;font-size:10.5px;gap:4px}
  .spray-label .brand-dot{width:8px;height:8px;border-width:1px}
  .spray-label .line-name{margin-top:8px;font-size:11.5px}
  .spray-label .line-sub{margin-top:3px;font-size:6.5px}
  .spray-label .band{margin-top:8px;height:17px;font-size:8.5px}
  .spray-label .volume{margin-top:10px;font-size:5.5px}

  /* dropper bottle label */
  .dropper-label{left:862px;top:233px;width:109px;height:180px}
  .dropper-label .panel{left:34px;top:64px;width:72px;height:96px}
  .dropper-label .brand{margin-top:9px;font-size:7.5px;gap:3px}
  .dropper-label .brand-dot{width:6px;height:6px;border-width:1px}
  .dropper-label .line-name{margin-top:5px;font-size:8.5px}
  .dropper-label .line-sub{margin-top:2px;font-size:4.8px}
  .dropper-label .band{margin-top:5px;height:12px;font-size:5.5px}
  .dropper-label .volume{margin-top:6px;font-size:4.5px}

  /* jar lid */
  .jar-lid{left:551px;top:383px;width:186px;height:186px;border-radius:50%;background:var(--ink);overflow:hidden}
  .jar-lid .lid-art{left:9px;top:9px;width:168px;height:168px;border-radius:50%}
  .jar-lid .lid-brand{position:absolute;left:9px;top:79px;width:71px;height:45px;background:var(--paper);
    display:flex;align-items:center;justify-content:center;gap:4px;font-family:"Lato",sans-serif;font-size:10.5px;color:var(--ink)}
  .jar-lid .lid-brand .brand-dot{width:8px;height:8px;border-width:1px}
  .jar-lid .lid-title{position:absolute;left:80px;top:63px;width:71px;height:56px;background:var(--coral);
    color:var(--paper);font-family:"Cinzel",serif;font-weight:600;font-size:7.5px;letter-spacing:.05em;
    line-height:1.35;display:flex;align-items:center;justify-content:center;text-align:center;text-transform:uppercase}
</style>
</head>
<body>
<main class="canvas">

  <section class="piece spray-label">
    <div class="pattern" style="inset:0" role="img" aria-label="Bohemian floral doodle print in coral, cream, pink and gold"></div>
    <div class="panel">
      <div class="brand"><span class="brand-dot"></span>MAVRA &amp; CO.</div>
      <div class="line-name">DERMAVELLE</div>
      <div class="line-sub">Baobin Collection</div>
      <div class="band">Balancing Toner</div>
      <div class="volume">200 ML</div>
    </div>
  </section>

  <section class="piece tall-box">
    <div class="pattern" style="inset:0" role="img" aria-label="Bohemian floral doodle print in coral, cream, pink and gold"></div>
    <div class="panel">
      <div class="brand"><span class="brand-dot"></span>MAVRA &amp; CO.</div>
      <div class="line-name">DERMAVELLE</div>
      <div class="line-sub">Baobin Collection</div>
      <div class="band">Balancing Toner</div>
      <div class="volume">200 ML</div>
    </div>
  </section>

  <section class="piece short-box">
    <div class="pattern" style="inset:0" role="img" aria-label="Bohemian floral doodle print in coral, cream, pink and gold"></div>
    <div class="panel">
      <div class="brand"><span class="brand-dot"></span>MAVRA &amp; CO.</div>
      <div class="line-name">DERMAVELLE</div>
      <div class="line-sub">Baobin Collection</div>
      <div class="band">Moisturizing Cream</div>
      <div class="volume">200 ML</div>
    </div>
  </section>

  <section class="piece jar-lid">
    <div class="pattern lid-art" role="img" aria-label="Bohemian floral doodle print on the jar lid"></div>
    <div class="lid-brand"><span class="brand-dot"></span>MAVRA &amp; CO.</div>
    <div class="lid-title">Luminous<br>Mineral<br>Foundation</div>
  </section>

  <section class="piece dropper-label">
    <div class="pattern" style="inset:0" role="img" aria-label="Bohemian floral doodle print in coral, cream, pink and gold"></div>
    <div class="panel">
      <div class="brand"><span class="brand-dot"></span>MAVRA &amp; CO.</div>
      <div class="line-name">DERMAVELLE</div>
      <div class="line-sub">Baobin Collection</div>
      <div class="band">Cleansing Oil</div>
      <div class="volume">120 ML</div>
    </div>
  </section>

  <section class="piece lip-box">
    <div class="pattern" style="inset:0" role="img" aria-label="Bohemian floral doodle print in coral, cream, pink and gold"></div>
    <div class="panel">
      <div class="brand"><span class="brand-dot"></span>MAVRA &amp; CO.</div>
      <div class="lip-title">Moisturizing<br>Lip Stick</div>
    </div>
  </section>

</main>
</body>
</html>
```